Rusty Lantern Bar & Grill Takeout Menu

Please create a takeout menu using the attached dine-in menu.
Take out menu size: Tri-Fold 11x17

Industry/Entity Type

Bar & Grill (Restaurant)

Colors

Designer to choose colors to be used in the design.

Requirements
Must have
• Phone number and website. "Order Online" "Order for Delivery"
Nice to have
• Area on the back of the menu to feature happy hour specials.

```html
<!DOCTYPE html>
<html lang="en">
<head>
<meta charset="utf-8">
<title>Rusty Lantern Bar &amp; Grill — Takeout Menu</title>
<link href="https://fonts.googleapis.com/css2?family=Almendra+SC&family=Josefin+Sans:wght@300;400;700&family=Rye&display=swap" rel="stylesheet">
<style>
:root{
  --purple:#2f2170;
  --purple-deep:#271a5e;
  --yellow:#efbd40;
  --yellow-bright:#f7c93f;
  --cream:#fff6dc;
  --ink:#2a1c63;
  --red:#d8452e;
  --page:#e3e2e6;
  --white:#ffffff;
}
*{box-sizing:border-box;margin:0;padding:0}
html,body{width:1018px;height:1200px;overflow:hidden}
body{background:var(--page);font-family:"Josefin Sans",sans-serif;font-weight:300;position:relative}
.sheet{position:absolute;left:96px;width:827px;height:535px;display:flex}
.sheet--outside{top:58px}
.sheet--inside{top:618px}
.panel{position:relative;height:100%;padding:32px 28px 0 30px}
.panel--purple{background:var(--purple);color:var(--white)}
.panel--yellow{background:var(--yellow);color:var(--ink)}
.w276{width:276px}.w269{width:269px}.w282{width:282px}
.heading{font-family:"Almendra SC",serif;font-weight:400;font-size:15px;line-height:1.4;letter-spacing:.3px}
.panel--yellow .heading{color:var(--ink)}
.intro{font-size:6.3px;line-height:1.55;margin-top:8px}
.sub{font-size:6.3px;line-height:1.5}
.row{display:flex;align-items:baseline;font-weight:700;font-size:6.6px;line-height:1.5}
.leader{flex:1;border-bottom:1px dotted currentColor;margin:0 2px;transform:translateY(-2px);opacity:.8}
.item{margin-top:7px}
.item .desc{font-size:6.3px;line-height:1.55}
.fine{font-size:4.6px;line-height:1.5}
.disclaimer{position:absolute;left:0;right:0;bottom:15px;text-align:center;font-size:4.3px;line-height:1.45;opacity:.9}
.label{font-weight:700;font-size:6.8px;text-decoration:underline;margin-top:11px}

/* burgers */
.proteins{position:absolute;left:155px;top:168px;width:88px;height:18px;border-radius:9px;background:var(--white);display:flex;justify-content:space-around;align-items:center}
.proteins span{width:10px;height:10px;border-radius:50%;border:1.2px solid var(--purple)}
.burger-table{position:absolute;left:30px;top:196px;width:216px;height:275px;background:var(--purple-deep);padding:6px 6px 0 7px}
.burger{display:grid;grid-template-columns:1fr 32px 32px 26px;font-size:5.6px;line-height:1.5;margin-bottom:5px}
.burger b{font-weight:700;display:block}
.burger .price{text-align:left;font-size:5.2px}

/* handhelds extras */
.tagbox{background:var(--yellow-bright);border-radius:5px;padding:4px 5px;color:var(--ink)}
.tagbox h3{font-family:"Almendra SC",serif;font-weight:400;font-size:10px;line-height:1.1}
.tagbox p{font-size:4.4px;line-height:1.5}
.extras{display:grid;grid-template-columns:97px 113px;gap:5px;margin-top:8px}
.bowl-art{position:absolute;left:172px;top:354px;width:70px;height:50px;border-radius:0 0 35px 35px;background:rgba(42,28,99,.12)}
.sides{font-weight:700;font-size:6.8px;line-height:1.6}

/* cover */
.cover{padding:0;width:276px;text-align:center}
.brand{position:absolute;top:22px;left:0;right:0;font-family:"Almendra SC",serif;color:var(--white);font-size:13px;line-height:1.2}
.band{position:absolute;left:7px;right:7px;height:9px;background:var(--yellow);opacity:.55}
.menu-word{position:absolute;top:112px;left:0;right:0;font-family:"Rye",serif;color:var(--yellow-bright);font-size:62px;line-height:1;letter-spacing:-1px;text-shadow:3px 3px 0 #120a33}
.stars{position:absolute;top:190px;left:70px;right:70px;display:flex;align-items:center;gap:6px}
.stars i{flex:1;height:1px;background:#9c93c9}
.stars svg{display:block}
.art-cover{position:absolute;top:231px;left:0;width:100%;height:193px;background:linear-gradient(135deg,var(--red),#c9462f 55%,#e3a27a)}
.order{position:absolute;top:424px;left:0;right:0;bottom:0;background:var(--yellow-bright);color:var(--ink);text-align:center;padding-top:19px}
.order h2{font-family:"Josefin Sans",sans-serif;font-weight:700;font-size:26px;line-height:1;letter-spacing:.5px;color:var(--purple)}
.order .web{font-weight:700;font-size:16px;margin-top:8px;color:#15103a}
.order .phone{font-family:"Rye",serif;font-size:15px;margin-top:5px;color:#15103a}

/* inside */
.addbox{position:absolute;left:0;right:0;top:366px;height:86px;background:var(--purple-deep);padding:10px 28px 0 30px;font-size:6.6px;line-height:1.55}
.addbox b{font-weight:700}
.pasta-art{position:absolute;left:76px;top:384px;width:120px;height:62px;border-radius:50%;background:rgba(42,28,99,.12)}
.art-inside{position:absolute;top:0;left:0;width:100%;height:158px;background:linear-gradient(120deg,#e88a2e,#f2c84a 45%,#e7602f)}
.drinks-art{position:absolute;right:22px;top:354px;width:52px;height:118px;border-radius:4px;background:rgba(255,255,255,.1)}
.soups{position:absolute;top:180px;left:30px;right:62px}
</style>
</head>
<body>

<!-- Outside of the tri-fold -->
<section class="sheet sheet--outside">
  <div class="panel panel--purple w276">
    <h2 class="heading">Gourmet Burgers &amp;<br>Sandwiches</h2>
    <p class="intro">Start with your style and then choose your protein. Our burgers are house made and cooked to your temperature. Our Fresh grilled chicken breast is marinated in house and cooked to perfection. Keep it vegetarian by choosing a vegetarian style along with the Quinoa Lentil Burger. All are served on a potato bun with lettuce, tomato, onion, and your choice of hand cut fries or sweet potato fries. Premium sides available for an up charge + $2</p>
    <div class="proteins" role="img" aria-label="Beef, chicken and vegetarian columns"><span></span><span></span><span></span></div>
    <div class="burger-table">
      <div class="burger"><div><b>Calico Cat</b>Roasted red peppers, red onions, brie cheese, and horseradish aioli.</div><span class="price">15.00*</span><span class="price">14.00</span><span class="price">13.00</span></div>
      <div class="burger"><div><b>Tiger Cat</b>Cheddar, Monterey Jack, and Provolone</div><span class="price">15.00*</span><span class="price">14.00</span><span class="price">13.00</span></div>
      <div class="burger"><div><b>Cat Scratch Fever</b>Guacamole, 3 pepper colby jack, pico de gallo, and chipotle mayo.</div><span class="price">15.50*</span><span class="price">15.00</span><span class="price">14.00</span></div>
      <div class="burger"><div><b>The Fat Cat</b>Fried egg*, bacon, cheddar cheese, and garlic aioli.</div><span class="price">16.00*</span><span class="price">15.50</span><span class="price">14.50</span></div>
      <div class="burger"><div><b>Tabby Cat</b>Melted brie cheese, sliced apple, and citrus aioli.</div><span class="price">16.50*</span><span class="price">15.50</span><span class="price">14.50</span></div>
      <div class="burger"><div><b>The Sphynx</b>Portobello mushrooms, roasted red peppers, smoked gouda cheese, and roasted garlic aioli.</div><span class="price">16.50*</span><span class="price">15.50</span><span class="price">14.50</span></div>
      <div class="burger"><div><b>Maine Coon</b>Grilled shrimp*, roasted corn, swiss cheese, and roasted garlic aioli.</div><span class="price">16.50*</span><span class="price">15.50</span><span class="price">14.50</span></div>
      <div class="burger"><div><b>Alley Cat</b>Whats up your alley? Choose a cheese, condiment and one topping. Additional Toppings $1 | Bacon, Egg, Shrimp - $2</div><span class="price">14.00*</span><span class="price">13.00</span><span class="price">12.00</span></div>
    </div>
    <p class="disclaimer">*The consumption of raw or undercooked eggs, meat, poultry, seafood or shellfish<br>may contribute to food borne illness, especially if you have a medical condition.<br>– Vegetarian &nbsp;– Spicy</p>
  </div>

  <div class="panel panel--yellow w276">
    <h2 class="heading">Other Handhelds:</h2>
    <p class="sub">All served with Hand Cut Fries or Sweet Potato Fries.<br>Premium sides available for an up charge +2</p>
    <div class="item" style="margin-top:12px"><div class="row">Cat Club<span class="leader"></span>15</div><p class="desc">Sliced whole wheat bread with roasted garlic aioli, grilled marinated chicken breast, provolone cheese bacon, lettuce and tomato.</p></div>
    <div class="item"><div class="row">Southwest Melt<span class="leader"></span>14</div><p class="desc">Sliced whole wheat bread with roasted garlic aioli,3 pepper colby jack, roasted red peppers and corn.</p></div>
    <div class="item"><div class="row">What's Gouda?<span class="leader"></span>14</div><p class="desc">Sliced whole wheat bread with roasted garlic aioli smoked gouda and provolone cheeses, roasted red peppers and portobello mushrooms.</p></div>
    <div class="item"><div class="row">Westover Melt<span class="leader"></span>14</div><p class="desc">Sliced whole wheat bread with roasted garlic aioli, zucchini, portobello mushrooms, red peppers, with melted brie and provolone cheeses.</p></div>
    <div class="extras">
      <div class="tagbox"><h3>Cheeses:</h3><p>Vermont Cheddar | Smoked Gouda 3-Pepper Colby Jack Monterey Jack | Swiss | Brie Provolone | American</p></div>
      <div class="tagbox"><h3>Toppings:</h3><p>Bacon | Shrimp | Egg | Red Onion | White Onion | Portobello Mushrooms | Roasted Corn | Roasted Red Pepper Guacamole | Pico De Gallo | Fresh or Pickled Jalapenos</p></div>
      <div class="tagbox"><h3>Condiments:</h3><p>Horseradish Aioli | Chipotle Crema | Roasted Garlic Aioli | Citrus Aioli Spicy Ketchup | Dijon Mustard | Yellow Mustard | Mayo | Ketchup</p></div>
    </div>
    <div class="bowl-art" role="img" aria-label="Line sketch of a salad bowl"></div>
    <h2 class="heading" style="margin-top:10px">Sides:</h2>
    <p class="sides">Potato Salad $4 &nbsp;| Fire Roasted Veggies $6<br>Brown Rice, Quinoa, &amp; Kale Medley $5</p>
    <h2 class="heading" style="margin-top:10px">Kids Menu:</h2>
    <p class="sub">All served with French Fries</p>
    <div class="row" style="margin-top:5px">Grilled Cheese<span class="leader"></span>8</div>
    <div class="row" style="margin-top:4px">Cheese Queradilla<span class="leader"></span>8</div>
    <div class="row" style="margin-top:4px">Mac &amp; Cheese<span class="leader"></span>8</div>
    <div class="row" style="margin-top:4px">Chicken Tenders<span class="leader"></span>10</div>
    <p class="disclaimer">*The consumption of raw or undercooked eggs, meat, poultry, seafood or shellfish<br>may contribute to food borne illness, especially if you have a medical condition.<br>– Vegetarian &nbsp;– Spicy</p>
  </div>

  <div class="panel panel--purple cover">
    <p class="brand">Rusty Lantern<br>Bar &amp; Grill</p>
    <div class="band" style="top:95px"></div>
    <p class="menu-word">MENU</p>
    <div class="stars"><i></i>
      <svg width="34" height="8" viewBox="0 0 34 8" aria-hidden="true"><g fill="#9c93c9"><polygon points="4,1 5,3.5 7.5,3.6 5.6,5.1 6.3,7.6 4,6.1 1.7,7.6 2.4,5.1 .5,3.6 3,3.5"/><polygon points="17,0 18.3,3 21.5,3.1 19,5 19.9,8 17,6.2 14.1,8 15,5 12.5,3.1 15.7,3"/><polygon points="30,1 31,3.5 33.5,3.6 31.6,5.1 32.3,7.6 30,6.1 27.7,7.6 28.4,5.1 26.5,3.6 29,3.5"/></g></svg>
      <i></i></div>
    <div class="band" style="top:209px"></div>
    <div class="art-cover" role="img" aria-label="Painted illustration of cartoon cats eating burgers and drinking at a bar table"></div>
    <div class="order">
      <h2>ORDER DELIVERY</h2>
      <p class="web">WWW.RUSTYLANTERNGRILL.COM</p>
      <p class="phone">555-014-7270</p>
    </div>
  </div>
</section>

<!-- Inside of the tri-fold -->
<section class="sheet sheet--inside">
  <div class="panel panel--purple w276">
    <h2 class="heading" style="margin-top:-9px">Salads</h2>
    <div class="item" style="margin-top:17px"><div class="row" style="width:160px">Combo Cat<span class="leader"></span>11</div><p class="desc">Enjoy a side House and a cup of any soup.</p></div>
    <div class="item" style="margin-top:12px"><div class="row" style="width:160px">Cat House Salad<span class="leader"></span>11</div><p class="desc">Spring lettuce mix, fresh red peppers, onion, cherry tomatoes, cucumber, and croutons. Served with Red Wine Vinaigrette.</p></div>
    <div class="item" style="margin-top:12px"><div class="row" style="width:160px">Grilled Chicken Salad<span class="leader"></span>15</div><p class="desc">Spring lettuce mix, grilled chicken breast, bacon,<br>fresh red peppers, onions, tomatoes, cucumber and<br>feta cheese. Served with Red Wine Vinaigrette</p></div>
    <div class="item" style="margin-top:12px"><div class="row" style="width:160px">Grilled Shrimp Salad*<span class="leader"></span>16</div><p class="desc">Spring lettuce mix, garlic Roasted Shrimp, roasted corn,<br>pico de gallo fresh avocado. Served with<br>Lemon Champagne Vinaigrette</p></div>
    <div class="item" style="margin-top:12px"><div class="row" style="width:160px">Goat Cheese Salad<span class="leader"></span>16</div><p class="desc">Spring lettuce mix, fried goat cheese, fresh red peppers,<br>cranberries, white onions, and cherry tomatoes.<br>Served with Lemon Champagne Vinaigrette.</p></div>
    <div class="item" style="margin-top:12px"><div class="row" style="width:160px">The Skinny Cat<span class="leader"></span>14</div><p class="desc">Spring lettuce mix, sliced apple, sun dried cranberries,<br>roasted corn, cherry tomatoes, and feta cheese.<br>Served with Balsamic Vinaigrette.</p></div>
    <div class="row" style="width:160px;margin-top:12px">Small House Salad<span class="leader"></span>6</div>
    <div class="addbox">
      <p><b>Add: &nbsp;Grilled Chicken &nbsp;5 | Garlic Roasted Shrimp 5<br>Fried Goat Cheese 4 , Fried Goat Cheese 5</b></p>
      <p style="margin-top:9px"><b>Dressings</b><br>Balsamic Vinaigrette | Caesar | Red Wine Vinaigrette<br>Honey-Mustard | Lemon Champagne Vinaigrette | Ranch | Blue Cheese</p>
    </div>
    <p class="disclaimer">*The consumption of raw or undercooked eggs, meat, poultry, seafood or shellfish<br>may contribute to food borne illness, especially if you have a medical condition.<br>– Vegetarian &nbsp;– Spicy</p>
  </div>

  <div class="panel panel--yellow w269">
    <h2 class="heading" style="margin-top:-8px">Starters</h2>
    <p class="label" style="margin-top:10px">TORTILLA CHIPS:</p>
    <div style="width:178px;margin-top:4px">
      <div class="row">with House-made Salsa Verde<span class="leader"></span>7</div>
      <div class="row">with House-made Fire Roasted Salsa<span class="leader"></span>7</div>
      <div class="row">with Guacamole &amp; Pico De Gallo<span class="leader"></span>8</div>
      <div class="row">with Queso<span class="leader"></span>8</div>
      <div class="row">with Chili con Queso<span class="leader"></span>9</div>
    </div>
    <p class="label">WINGS:</p>
    <div class="row" style="width:182px;margin-top:4px">8 pieces<span class="leader"></span>14</div>
    <p class="fine" style="width:190px">Flash-fried to a crispy golden brown and tossed in your choice of sauce. Choose from our Signature Hot, or Mild Sauce, or BBQ. Your choice of ranch or blue cheese.</p>
    <p class="label">QUESADILLAS:</p>
    <div style="width:182px;margin-top:4px">
      <div class="row">Cheddar and Monterey Jack Cheese<span class="leader"></span>12</div>
      <div class="row">Pulled Marinated Chicken &amp; Cheese<span class="leader"></span>16</div>
      <div class="row">Fire Roasted Vegetables &amp; Cheese<span class="leader"></span>14</div>
      <div class="row">Garlic Roasted Shrimp &amp; Cheese<span class="leader"></span>16</div>
    </div>
    <p class="fine" style="width:190px">All quesadillas are stuffed with roasted red peppers, black beans and your choice below. Served with guacamole, pico de gallo, and chipotle crema on the side.</p>
    <p class="label" style="margin-top:8px">CLAW-FULL NACHOS:</p>
    <p class="fine" style="width:190px">Tortilla chips, melted white queso, Cheddar and Monterey Jack cheeses, pico de gallo, guacamole, chipotle sour cream, jalapenos, black beans, &amp; green onions</p>
    <div style="width:180px">
      <div class="row" style="margin-top:5px">Rusty Lantern Chili Nachos<span class="leader"></span>14</div>
      <div class="row" style="margin-top:5px">Pulled Chicken Nachos<span class="leader"></span>16</div>
      <div class="row" style="margin-top:5px">Garlic Roasted Shrimp<span class="leader"></span>16</div>
      <div class="row" style="margin-top:5px">Fire Roasted Vegetables Nachos<span class="leader"></span>14</div>
    </div>
    <p class="desc" style="font-size:6.3px">Portobello, Red Peppers, &amp; Zucchini</p>
    <div class="pasta-art" role="img" aria-label="Line sketch of a plate of pasta"></div>
    <p class="disclaimer">*The consumption of raw or undercooked eggs, meat, poultry, seafood or shellfish<br>may contribute to food borne illness, especially if you have a medical condition.<br>– Vegetarian &nbsp;– Spicy</p>
  </div>

  <div class="panel panel--purple w282">
    <div class="art-inside" role="img" aria-label="Painted illustration of two cartoon cats sharing food and drinks at a table"></div>
    <div class="soups">
      <p class="row" style="text-decoration:underline">FRENCH FRIES:</p>
      <p class="desc" style="font-size:6.3px">Served with our house made Garlic Aioli and Spicy Ketchup.</p>
      <div class="row" style="margin-top:6px">Fries Only<span class="leader"></span>7</div>
      <div class="row" style="margin-top:5px">Sweet Potato Fries<span class="leader"></span>7</div>
      <div class="row" style="margin-top:5px">Cheddar-Jack Cheese Fries<span class="leader"></span>8</div>
      <div class="row" style="margin-top:5px">Cheddar-Jack Cheese, Bacon Fries<span class="leader"></span>9</div>
      <div class="row" style="margin-top:5px">Chili Cheese Fries<span class="leader"></span>10</div>
      <p class="fine">Topped with Rusty Lantern Chili, cheddar jack cheese and served with chipotle crema on the side.</p>
      <div class="row" style="margin-top:9px">Rusty Lantern Chili<span class="leader"></span>Cup 6 | Bowl 8</div>
      <p class="fine">Signature Chili with lean ground beef, black beans, and corn. Topped with cheddar cheese and green onion, served with tri-color tortilla chips.</p>
      <div class="row" style="margin-top:7px">Southwestern Sweet Potato Soup ...... Cup 6 | Bowl 8</div>
      <p class="fine">A delicious mix of sweet potatoes, corn, bell peppers, and black beans, this vegan soup delivers top flavor and quality with every bowl. Served with tri-color tortilla chips.</p>
      <div class="row" style="margin-top:11px">Ancient Grains Bowl<span class="leader"></span>12</div>
      <p class="fine">Quinoa, brown rice, kale and fresh spinach, with fire roasted portobello mushrooms, zucchini and red peppers. Topped with fresh avocado, and feta cheese. Served with Lemon Champagne Vinaigrette</p>
      <p class="row" style="margin-top:10px">Add: &nbsp;Grilled Chicken &nbsp;5 | Garlic Roasted Shrimp 5</p>
    </div>
    <div class="drinks-art" role="img" aria-label="Line sketch of cocktail glasses and berries"></div>
    <p class="disclaimer">*The consumption of raw or undercooked eggs, meat, poultry, seafood or shellfish<br>may contribute to food borne illness, especially if you have a medical condition.<br>– Vegetarian &nbsp;– Spicy</p>
  </div>
</section>

</body>
</html>
```